The Burrow On Maple "Neighborhood Tavern" - Menu Re-Design

HI,
I am a restaurant owner in Los Angeles, CA and I need to overhaul my food & drink menus. I would like something more creative than what I currently have. Please keep in mind that this is a neighborhood bar & tavern on the Maple Row in Los Angeles. We are not a fine dining establishment, diner or sports bar. Please view our website to get a feel for the current brand identity http://www.theburrowonmaple.com
I will upload our current menu which is simple and our previous design which was more involved. I would like this new menu design to be fun and engage our customers to order more food and drink.
Lastly I would like to be able to update the content easily.
Additional Info based on designer questions added 8-20-15:
Preferred size is 8.5x14 in. / legal size.
I do not want food pics on the menu but artistic food and drink drawings are okay.
The link below has logo files and the previous menu file in AI.
https://files.quorvashare.com/u/517608/Menu%20Re-Design%20Reference%20Folder.zip
Industry/Entity Type
Restaurant
Requirements
Must have
- be editable by my staff which has basic AI knowledge
Should not have
- food photos

```html
<!DOCTYPE html>
<html lang="en">
<head>
<meta charset="utf-8">
<title>The Burrow On Maple – Sunday BBQ</title>
<link href="https://fonts.googleapis.com/css2?family=Oswald:wght@400;500;600;700&family=Roboto+Condensed:wght@400;700&display=swap" rel="stylesheet">
<style>
  :root {
    --brick: #8e2b2f;
    --brick-dark: #6f1f23;
    --ink: #2b1c1c;
    --paper: #ffffff;
    --sketch: #d9c9bd;
  }
  * { box-sizing: border-box; margin: 0; padding: 0; }
  html, body { width: 778px; height: 1200px; overflow: hidden; background: var(--paper); }
  .menu { position: relative; width: 778px; height: 1200px; background: var(--paper); color: var(--ink); font-family: "Roboto Condensed", sans-serif; }

  .hours { position: absolute; left: 34px; top: 30px; width: 220px; font-family: "Oswald", sans-serif; font-weight: 700; color: var(--brick); font-size: 23px; line-height: 1.3; text-transform: uppercase; }

  .brand { position: absolute; left: 272px; top: 0; width: 234px; height: 290px; display: flex; flex-direction: column; align-items: center; justify-content: center; gap: 10px; border-left: 4px solid var(--brick); border-right: 4px solid var(--brick); border-bottom: 4px solid var(--brick); }
  .brand-mark { width: 26px; height: 26px; background: var(--brick); }
  .brand-name { font-family: "Oswald", sans-serif; font-weight: 700; color: var(--brick); font-size: 40px; line-height: 1.05; text-align: center; text-transform: uppercase; }

  .sketch { position: absolute; left: 530px; top: 8px; width: 220px; height: 270px; background: linear-gradient(180deg, #efe5de, var(--sketch)); }

  .banner { position: absolute; left: 210px; top: 318px; width: 358px; text-align: center; z-index: 2; background: var(--paper); }
  .banner-title { border: 4px solid var(--brick); font-family: "Oswald", sans-serif; font-weight: 700; font-size: 44px; line-height: 54px; color: var(--ink); text-transform: uppercase; letter-spacing: 1px; }
  .banner-note { display: flex; justify-content: space-between; background: var(--brick); color: var(--paper); font-family: "Oswald", sans-serif; font-size: 17px; padding: 3px 16px; text-transform: uppercase; }

  .board { position: absolute; left: 30px; top: 392px; width: 718px; height: 740px; border: 4px solid var(--brick); padding: 56px 30px 0; text-align: center; }
  .dish { margin-bottom: 26px; }
  .dish-name { font-family: "Oswald", sans-serif; font-weight: 700; font-size: 33px; line-height: 1.1; text-transform: uppercase; color: var(--ink); margin-bottom: 6px; }
  .dish-desc { font-size: 19px; line-height: 1.3; }

  .sides-head { display: flex; align-items: center; justify-content: center; gap: 12px; font-family: "Oswald", sans-serif; font-weight: 700; font-size: 30px; text-transform: uppercase; margin: 8px 0 14px; }
  .sides-head svg { width: 20px; height: 14px; }
  .sides { display: grid; grid-template-columns: 1fr 1fr; gap: 4px 24px; font-size: 19px; line-height: 1.3; }

  .footer-band { position: absolute; left: 30px; top: 1138px; width: 718px; height: 28px; background: var(--brick); color: var(--paper); font-family: "Oswald", sans-serif; font-size: 15px; letter-spacing: 1.5px; text-transform: uppercase; display: flex; align-items: center; justify-content: center; }
  .footer-links { position: absolute; left: 0; top: 1172px; width: 778px; text-align: center; font-size: 14px; color: var(--brick); letter-spacing: 0.5px; }
</style>
</head>
<body>
<div class="menu">
  <div class="hours">Hours:<br>Mon–Fri:<br>5pm–2am<br>Sat: 3pm–2am<br>Sun: 12pm–2am<br>DJ Friday<br>&amp; Saturday<br>10pm–2am</div>

  <div class="brand">
    <span class="brand-mark"></span>
    <span class="brand-name">The Burrow<br>On Maple</span>
  </div>

  <div class="sketch" role="img" aria-label="Sketch of a man in a hat standing with a small dog"></div>

  <div class="banner">
    <div class="banner-title">Sunday BBQ</div>
    <div class="banner-note"><span>Served from noon</span><span>Until sold out</span></div>
  </div>

  <section class="board">
    <div class="dish">
      <h2 class="dish-name">Bratwurst</h2>
      <p class="dish-desc">Simmered in Beer, Ale Soaked Onions, Whole Grain Mustard<br>Served on a Kaiser Bun 6</p>
    </div>
    <div class="dish">
      <h2 class="dish-name">Cheeseburger</h2>
      <p class="dish-desc">100% Grass Fed Beef, Cheddar or Pepper Jack Cheese, Shaved<br>Red Onions, Pickles, Tomato, Lettuce, Brioche Bun,<br>House Sauce 10<br>+ Avocado / Bacon 2 each</p>
    </div>
    <div class="dish">
      <h2 class="dish-name">Baby Back Ribs</h2>
      <p class="dish-desc">1/3 Rack, Dry Rubbed, House-Made Sweet<br>Barbecue Sauce 10</p>
    </div>
    <div class="dish">
      <h2 class="dish-name">Half Chicken</h2>
      <p class="dish-desc">Garlic Chile Cured, House-Made Sweet<br>Barbecue Sauce 10</p>
    </div>
    <h3 class="sides-head">
      <svg viewBox="0 0 20 14"><polygon points="0,0 20,0 10,14" fill="var(--brick)"/></svg>
      Sides
      <svg viewBox="0 0 20 14"><polygon points="0,0 20,0 10,14" fill="var(--brick)"/></svg>
    </h3>
    <div class="sides">
      <p>Smoked Baked Beans with<br>Applewood Bacon 4</p>
      <p>Creamy Potato Salad with Bacon 4<br>Grilled Asparagus 4</p>
    </div>
  </section>

  <div class="footer-band">Book your next event here! info@theburrowonmaple.com</div>
  <div class="footer-links">@burrowonmaple &nbsp; www.theburrowonmaple.com</div>
</div>
</body>
</html>
```